栃木県の幹線道路50号線に2ヵ所野立て看板のデザインをお願いします。
参考デザインはあります。
車の通行量が1日2万台通りますので、一目でとんかつ屋があることを伝いたいです。

資料写真はあります。
少女系アニメキャラクターを入れた看板なんかも目を引いて面白いと思います。
記載項目
こだわりとんかつ翠嶺
新潟タレかつ丼!
特選から揚げ!
ご飯・キャベツ・味噌汁お代わり無料
150m先左
お持ち帰り弁当・宅配もやってます。
看板サイズH1800×W900

こだわりとんかつ翠嶺
新潟タレかつ丼
特選から揚げ
ご飯・キャベツ・味噌汁お代わり無料
直進2Km先右側
看板サイズH2400×W2700
黄・オレンジ系

当店のイメージに合ってました。

今回は、ご提案頂きましてありがとうございました。
どの提案もとてもよかったです。大変迷いましたが決めさせていただきました。
次の機会もお願いいたします。

```html
<!DOCTYPE html>
<html lang="ja">
<head>
<meta charset="utf-8">
<title>こだわりとんかつ翠嶺 野立て看板</title>
<link href="https://fonts.googleapis.com/css2?family=Dela+Gothic+One&family=Noto+Sans+JP:wght@700;900&display=swap" rel="stylesheet">
<style>
:root{
  --band-red:#c8321e;
  --orange:#e8742a;
  --orange-deep:#d85a1c;
  --red:#d6201c;
  --cream:#f8f0e2;
  --cream-dark:#efe2cc;
  --ink:#1a1412;
  --yellow:#ffe14a;
  --white:#ffffff;
}
*{margin:0;padding:0;box-sizing:border-box}
html,body{width:1200px;height:2408px;overflow:hidden;background:var(--white)}
.sign{position:relative;width:1200px;height:2408px;overflow:hidden;
  background:linear-gradient(180deg,var(--cream) 0%,var(--cream-dark) 100%);
  font-family:"Noto Sans JP",sans-serif;color:var(--ink)}

.direction{position:absolute;left:0;top:0;width:1200px;height:100px;background:var(--band-red);
  display:flex;align-items:center;padding-left:20px;gap:16px;color:var(--white)}
.direction svg{width:76px;height:84px}
.direction .distance{font-weight:900;font-size:92px;line-height:1;letter-spacing:2px}
.direction .turn{margin-left:auto;margin-right:14px;width:90px;height:88px;border-radius:18px;background:var(--white);
  color:var(--ink);font-weight:900;font-size:76px;line-height:88px;text-align:center}

.takeout{position:absolute;left:0;top:100px;width:152px;height:1788px;background:var(--band-red);
  writing-mode:vertical-rl;text-align:center;padding:0 28px;
  color:var(--yellow);font-weight:900;font-size:96px;line-height:96px;letter-spacing:4px}

.headline-box{position:absolute;left:988px;top:160px;width:180px;height:880px;background:var(--white);
  border:8px solid var(--ink);writing-mode:vertical-rl;text-align:center;padding:0 36px;
  font-weight:900;font-size:92px;line-height:92px;letter-spacing:0}
.headline-box .accent{color:var(--red)}
.headline-box .bang{text-combine-upright:all;color:var(--red)}

.tonkatsu{position:absolute;left:640px;top:230px;width:240px;writing-mode:vertical-rl;
  font-family:"Dela Gothic One",sans-serif;font-weight:400;
  font-size:230px;line-height:240px;color:var(--orange);letter-spacing:0;
  text-shadow:5px 5px 0 var(--white),-4px -4px 0 var(--white)}

.kodawari{position:absolute;left:488px;top:272px;display:flex;flex-direction:column;gap:4px}
.kodawari span{display:block;width:92px;height:74px;background:var(--orange-deep);color:var(--white);
  font-weight:900;font-size:64px;line-height:74px;text-align:center}

.refill{position:absolute;left:240px;top:452px;font-weight:900;font-size:56px;line-height:1}
.free{position:absolute;left:228px;top:632px;font-weight:900;font-size:104px;line-height:1;color:var(--red)}
.free-reading{position:absolute;left:440px;top:598px;writing-mode:vertical-rl;font-weight:900;font-size:44px;line-height:1;color:var(--red)}

.items{position:absolute;writing-mode:vertical-rl;font-weight:900;font-size:52px;line-height:1}
.items.rice{left:290px;top:790px}
.items.soup{left:362px;top:950px}
.items.cabbage{left:430px;top:850px}

.shop-name{position:absolute;left:520px;top:760px;writing-mode:vertical-rl;
  font-weight:900;font-size:110px;line-height:1;color:var(--ink)}
.shop-name i{display:inline-block;width:34px;height:34px;border-radius:50%;background:var(--red);margin-top:14px}

.character{position:absolute;left:660px;top:1180px;width:540px;height:1228px;
  background:linear-gradient(180deg,#f3d0b4 0%,#c0684e 40%,#7a7478 100%);border-radius:250px 250px 0 0}
.food{position:absolute;left:160px;top:1160px;width:480px;height:600px;border-radius:50% 50% 34% 34%;
  background:radial-gradient(circle at 50% 35%,#e0a24a 0%,#a95a1e 55%,#4a2a18 100%)}
</style>
</head>
<body>
<main class="sign">
  <header class="direction">
    <svg viewBox="0 0 100 110" aria-hidden="true"><path d="M50 4 L96 52 H66 V106 H34 V52 H4 Z" fill="#ffffff"/></svg>
    <span class="distance">150m先</span>
    <span class="turn">左</span>
  </header>
  <div class="takeout">お持ち帰り弁当・宅配もやってます。</div>
  <div class="headline-box">新潟<span class="accent">タレ</span>かつ丼<span class="bang">!!</span></div>
  <h1 class="tonkatsu">とんかつ</h1>
  <div class="kodawari"><span>こ</span><span>だ</span><span>わ</span><span>り</span></div>
  <p class="refill">お代わり</p>
  <p class="free">無料</p>
  <p class="free-reading">タダ</p>
  <p class="items rice">・ご飯</p>
  <p class="items soup">味噌汁</p>
  <p class="items cabbage">・キャベツ</p>
  <div class="shop-name">翠嶺<i></i></div>
  <div class="character" role="img" aria-label="親指を立てて笑うアニメ風の女性キャラクターのイラスト"></div>
  <div class="food" role="img" aria-label="丼に盛られた新潟タレかつ丼の写真"></div>
</main>
</body>
</html>
```